Flat bootstrap design for existing site

I'm looking for a modern flat design based around an existing logo. This has to be a custom design (no external templates), and implemented into a bootstrap framework.

The logo is attached as 2 versions - choose whichever you want, that flows better with whatever design you choose.

Added screenshots of the existing site (currently using the default bootstrap layouts). Please make your designs around those pages in the screenshots (i.e. the homepage only has the postal code input and the header). The active page has 3 screenshots, because I wanted to illustrate the other states that would be visible (in the table rows).

This is a moving/junk removal website, just for some context.

Here's some example websites (flat designs) that I like, just to give you an idea of what I'm after.

https://www.plivoterra.com/
https://damsoqua.com/
https://trevalin.com/
https://morkadelphi.com/en/

Coding

Coded - Design and coding required

Number of Pages Required

5+ page

Colors

Designer to choose colors to be used in the design.

Requirements
Must have
• It must be a modern/simple flat design, that is built around the existing logo (attached).
• It has to be implemented using bootstrap.

```html
<!DOCTYPE html>
<html lang="en">
<head>
<meta charset="utf-8">
<title>HAULVO — Junk Removal</title>
<link rel="stylesheet" href="https://fonts.googleapis.com/css2?family=Open+Sans:wght@400;600;700&family=Raleway:wght@400;500&family=Roboto:wght@400&display=swap">
<style>
  :root {
    --sky: #38bdf3;
    --navy: #064b86;
    --green: #8cc63f;
    --white: #ffffff;
    --footer-text: #1d4f7a;
    --placeholder: #9a9aa6;
    --illus-teal: #4ab3c4;
    --illus-orange: #f2912b;
    --illus-shadow: #1f8fce;
    --social-a: #4a78d8;
    --social-b: #1fb0e8;
    --social-c: #9a6a4e;
  }
  * { box-sizing: border-box; margin: 0; padding: 0; }
  html, body { width: 1200px; height: 621px; overflow: hidden; }
  body { position: relative; background: var(--sky); font-family: "Open Sans", sans-serif; color: var(--white); }

  .site-header { position: absolute; top: 0; left: 0; width: 1200px; height: 90px; }
  .brand { position: absolute; left: 144px; top: 24px; font-family: "Open Sans", sans-serif; font-weight: 700; font-size: 38px; letter-spacing: 1px; color: var(--white); line-height: 1; }
  .main-nav { position: absolute; top: 38px; left: 620px; display: flex; gap: 27px; }
  .main-nav a { color: var(--white); text-decoration: none; font-weight: 600; font-size: 13.5px; position: relative; }
  .main-nav a.is-active::after { content: ""; position: absolute; left: 50%; margin-left: -6px; bottom: -7px; width: 12px; height: 2px; background: var(--white); }
  .btn-signin { position: absolute; left: 975px; top: 30px; width: 81px; height: 34px; background: var(--navy); border-radius: 3px; color: var(--white); font-weight: 600; font-size: 13.5px; display: flex; align-items: center; justify-content: center; text-decoration: none; }

  .hero { position: absolute; top: 166px; left: 300px; width: 514px; text-align: center; }
  .hero-title { font-family: "Raleway", sans-serif; font-weight: 500; font-size: 49px; line-height: 53px; letter-spacing: -0.5px; }
  .booking-form { position: absolute; top: 128px; left: 116px; display: flex; box-shadow: 0 6px 14px rgba(0,60,110,0.18); border-radius: 3px; overflow: hidden; }
  .postal-input { width: 191px; height: 50px; border: 0; padding-left: 16px; font-family: "Raleway", sans-serif; font-size: 13.5px; color: #333; background: var(--white); outline: none; }
  .postal-input::placeholder { color: var(--placeholder); }
  .btn-book { width: 94px; height: 50px; border: 0; background: var(--green); color: var(--white); font-family: "Open Sans", sans-serif; font-weight: 700; font-size: 13.5px; display: flex; align-items: center; justify-content: center; gap: 9px; }

  .hero-illustration { position: absolute; left: 805px; top: 98px; width: 285px; height: 312px; border-radius: 40px 40px 10px 10px; background: linear-gradient(180deg, var(--illus-orange) 0%, var(--illus-teal) 62%, var(--illus-shadow) 100%); opacity: 0.85; }

  .site-footer { position: absolute; left: 0; top: 556px; width: 1200px; height: 65px; background: var(--white); }
  .copyright { position: absolute; left: 144px; top: 24px; font-family: "Roboto", sans-serif; font-size: 13px; color: var(--footer-text); }
  .social-links { position: absolute; left: 987px; top: 22px; display: flex; gap: 6px; }
  .social-links span { display: block; width: 19px; height: 19px; border-radius: 2px; }
  .social-links .s1 { background: var(--social-a); }
  .social-links .s2 { background: var(--social-b); }
  .social-links .s3 { background: var(--social-c); }
</style>
</head>
<body>
  <header class="site-header">
    <div class="brand">HAULVO</div>
    <nav class="main-nav">
      <a href="#">BOOK</a>
      <a href="#">HOW IT WORKS</a>
      <a href="#" class="is-active">BECOME A DRIVER</a>
    </nav>
    <a href="#" class="btn-signin">SIGNIN</a>
  </header>

  <main class="hero">
    <h1 class="hero-title">Need junk removed?<br>Book now.</h1>
    <form class="booking-form">
      <input class="postal-input" type="text" placeholder="Postal Code">
      <button class="btn-book" type="button">BOOK
        <svg width="18" height="8" viewBox="0 0 18 8" aria-hidden="true"><path d="M0 4h16M13 1l3 3-3 3" stroke="#fff" stroke-width="1.3" fill="none"/></svg>
      </button>
    </form>
  </main>

  <div class="hero-illustration" role="img" aria-label="Illustration of a smiling junk removal worker riding a teal wheeled bin, with a broom and a full garbage bag beside it"></div>

  <footer class="site-footer">
    <p class="copyright">© 2017 HAULVO. All rights reserved.</p>
    <div class="social-links">
      <span class="s1"></span><span class="s2"></span><span class="s3"></span>
    </div>
  </footer>
</body>
</html>
```